Vantage Sport And Fitness- Rates

I am opening up a new Gym/Training Facility. The Name of my New gym is Vantage Sports And Fitness. I am wanting to design a card that captures Membership Pricing/Personal Training Pricing. I will Upload the Logo. My colors are Red/Black/Silver. I really want there pricing card to "POP". IT needs to be very Professional and Clean. I will be placing these cards on a 5'7 . I would like these item on the card:
Name of Company: Vantage Sports And Fitness
Address:
2817 Larkmoor Commerce Dr.
Suite 214 Chantilly, VA 20153
Phone #: 703-555-0187
website: www.vantagesnf-example.com
Membership Rates:
$99/Month
$49 Heroes Rate
Family Plan:
2 People $149
3 People $199
4 People $299
Personal Training Rates:
1 session $102
5 sessions $490
10 sessions $940
20 sessions $1,800
40 sessions $3,400
Please be creative

```html
<!DOCTYPE html>
<html lang="en">
<head>
<meta charset="utf-8">
<title>Vantage Sports And Fitness – Rates</title>
<link href="https://fonts.googleapis.com/css2?family=Montserrat:wght@500;700;800&family=Roboto+Slab:wght@400;500;700&display=swap" rel="stylesheet">
<style>
  :root {
    --header-dark: #3a3a3c;
    --header-darker: #242426;
    --silver-light: #f2f2f2;
    --silver-mid: #c9c9cb;
    --silver-dark: #8e8e90;
    --red: #e3222b;
    --red-deep: #b4141b;
    --box-red: #8f0f14;
    --box-red-edge: #6e0a0e;
    --ink: #1a1a1a;
    --white: #ffffff;
    --label-white: rgba(255,255,255,0.82);
  }
  * { margin: 0; padding: 0; box-sizing: border-box; }
  html, body { width: 857px; height: 1200px; overflow: hidden; background: #ffffff; }
  .rate-card {
    position: relative;
    width: 857px;
    height: 1200px;
    overflow: hidden;
    background: var(--red);
    font-family: "Roboto Slab", serif;
  }

  /* Header */
  .masthead {
    position: absolute; left: 0; top: 0; width: 857px; height: 148px;
    background: linear-gradient(180deg, var(--header-dark), var(--header-darker));
  }
  .brand {
    position: absolute; left: 40px; top: 36px; display: flex; align-items: center; gap: 16px;
  }
  .brand-dot {
    width: 68px; height: 68px; border-radius: 50%; background: var(--white);
  }
  .brand-name {
    font-family: "Montserrat", sans-serif; font-weight: 700; color: var(--white);
    line-height: 1;
  }
  .brand-name .main { display: block; font-size: 46px; letter-spacing: 1px; }
  .brand-name .sub { display: block; font-size: 15.5px; letter-spacing: 2.2px; margin-top: 6px; }
  .masthead-divider {
    position: absolute; left: 402px; top: 30px; width: 2px; height: 92px; background: rgba(255,255,255,0.55);
  }
  .contact {
    position: absolute; left: 420px; top: 32px;
    font-family: "Montserrat", sans-serif; font-weight: 500; color: var(--white);
    font-size: 15.5px; line-height: 23.5px; letter-spacing: 1.3px; text-transform: uppercase;
  }

  .silver-strip {
    position: absolute; left: 0; top: 148px; width: 857px; height: 30px;
    background: linear-gradient(180deg, #6d6d6f, #2b2b2d);
  }

  /* Hero photo area */
  .hero-photo {
    position: absolute; left: 0; top: 160px; width: 857px; height: 690px;
    background:
      radial-gradient(ellipse 300px 360px at 560px 340px, rgba(200,30,36,0.55), rgba(60,10,12,0) 70%),
      radial-gradient(ellipse 420px 420px at 470px 380px, #6a6a6c, #2c2c2e 60%, #151517 100%);
  }

  /* Membership tab */
  .section-band {
    position: absolute; left: 0; top: 808px; width: 857px; height: 40px;
    background: linear-gradient(180deg, var(--silver-dark), #5c5c5e);
  }
  .section-tab {
    position: absolute; left: 36px; top: 782px; width: 394px; height: 66px;
    background: linear-gradient(180deg, var(--silver-light), var(--silver-mid));
    border-radius: 16px 16px 0 0;
    display: flex; align-items: center; padding-left: 26px;
    font-weight: 500; font-size: 25px; letter-spacing: 1.5px; color: var(--ink);
  }

  /* Red price area */
  .rates {
    position: absolute; left: 0; top: 848px; width: 857px; height: 352px;
    background: linear-gradient(180deg, var(--red) 0%, var(--red) 55%, var(--red-deep) 100%);
  }
  .price-box {
    position: absolute;
    background: linear-gradient(180deg, var(--box-red), var(--box-red-edge));
    border-radius: 14px;
    color: var(--white);
    text-align: center;
    display: flex; flex-direction: column; justify-content: center; align-items: center;
    box-shadow: inset 0 0 0 2px rgba(0,0,0,0.15);
  }
  .price-box .amount { font-weight: 500; font-size: 50px; line-height: 1; }
  .price-box .label {
    font-weight: 400; font-size: 18px; letter-spacing: 1px; line-height: 1.1;
    color: var(--label-white); text-transform: uppercase; margin-top: 4px;
  }
  .price-box.heroes .label { font-size: 18px; }
  .price-box.training .amount { font-size: 40px; }
  .price-box.training .label { font-size: 14px; margin-top: 2px; }

  .plan-heading {
    position: absolute; left: 516px; top: 866px;
    font-weight: 500; font-size: 25px; letter-spacing: 2px; color: var(--ink);
  }

  .training-heading {
    position: absolute; left: 0; top: 1028px; width: 857px; height: 40px;
    display: flex; align-items: center;
  }
  .training-heading .rule { height: 3px; background: var(--white); }
  .training-heading .rule.left { width: 36px; }
  .training-heading .rule.right { flex: 1; }
  .training-heading .title {
    padding: 0 14px; font-weight: 500; font-size: 25px; letter-spacing: 2px; color: var(--white);
  }
</style>
</head>
<body>
<main class="rate-card">

  <header class="masthead">
    <div class="brand">
      <span class="brand-dot"></span>
      <div class="brand-name">
        <span class="main">VANTAGE</span>
        <span class="sub">SPORTS AND FITNESS</span>
      </div>
    </div>
    <div class="masthead-divider"></div>
    <address class="contact" style="font-style:normal">
      2817 Larkmoor Commerce Dr.<br>
      Suite 214 Chantilly, VA 20153<br>
      Phone #: 703-555-0187<br>
      Website: www.vantagesnf-example.com
    </address>
  </header>

  <div class="silver-strip"></div>

  <div class="hero-photo" role="img" aria-label="Dramatic black and white photo of a muscular athlete curling a dumbbell, lit with a red glow against a dark background"></div>

  <div class="section-band"></div>
  <h2 class="section-tab">MEMBERSHIP RATES:</h2>

  <section class="rates"></section>

  <div class="price-box" style="left:33px; top:893px; width:169px; height:123px;">
    <span class="amount">$99</span>
    <span class="label">/Month</span>
  </div>
  <div class="price-box heroes" style="left:214px; top:886px; width:131px; height:130px;">
    <span class="amount">$49</span>
    <span class="label">Heroes<br>Rate</span>
  </div>

  <h3 class="plan-heading">FAMILY PLAN</h3>
  <div class="price-box" style="left:369px; top:916px; width:164px; height:100px;">
    <span class="amount">$149</span>
    <span class="label">2 People</span>
  </div>
  <div class="price-box" style="left:543px; top:916px; width:150px; height:100px;">
    <span class="amount">$199</span>
    <span class="label">3 People</span>
  </div>
  <div class="price-box" style="left:690px; top:916px; width:160px; height:100px;">
    <span class="amount">$299</span>
    <span class="label">4 People</span>
  </div>

  <div class="training-heading">
    <span class="rule left"></span>
    <h3 class="title">PERSONAL TRAINING RATES</h3>
    <span class="rule right"></span>
  </div>

  <div class="price-box training" style="left:43px; top:1083px; width:136px; height:107px;">
    <span class="amount">$102</span>
    <span class="label">1 Session</span>
  </div>
  <div class="price-box training" style="left:190px; top:1083px; width:136px; height:107px;">
    <span class="amount">$490</span>
    <span class="label">5 Sessions</span>
  </div>
  <div class="price-box training" style="left:333px; top:1083px; width:136px; height:107px;">
    <span class="amount">$940</span>
    <span class="label">10 Sessions</span>
  </div>
  <div class="price-box training" style="left:476px; top:1083px; width:160px; height:107px;">
    <span class="amount">$1,800</span>
    <span class="label">20 Sessions</span>
  </div>
  <div class="price-box training" style="left:643px; top:1083px; width:166px; height:107px;">
    <span class="amount">$3,400</span>
    <span class="label">40 Sessions</span>
  </div>

</main>
</body>
</html>
```